Tallbrook Meridian Advisory needs business cards

Tallbrook Meridian Advisory is a new approach to consulting: we believe in partnering our clients in a hands-on, side-by-side, rolling-up-our sleeves approach, rather than being removed and aloof consultants.

We have a logo design developped through PixelHarbor (see attachment) and need to move to the stage of designing a business card for our 7 founding members.

Target Market(s)

Senior executives in local and global companies (such as Fizzmont Tonic, Hollanby, Brevard, etc)

Industry/Entity Type

Business

Requirements
Must have
• Look and feel: The design reflect the logo: i.e. professional, modern and approachable (as opposed to corporate traditional and remote). We are looking for a high quality, premium design.

Content must haves:
- prominent: our logo, person's name, function, phone number and e-mail address
- less prominent: company address and website

Example: Tallbrook Meridian Advisory logo, Mireille Vostag, Partner, +44 (0)781 209 3375, mireille_vostag@tallbrookmeridian.example / 17 Pelham Crescent, Brackwell, Eastshire, UK, BW4 3WN - www.tallbrookmeridian.example

- Both sides of the card can be used
- Both versions of the logo can be used (on black or on white)

```html
<!DOCTYPE html>
<html lang="en">
<head>
<meta charset="utf-8">
<title>Tallbrook Meridian Advisory – Business Cards</title>
<link rel="stylesheet" href="https://fonts.googleapis.com/css2?family=Lato:wght@400;700&display=swap">
<style>
  :root {
    --page-bg: #ffffff;
    --blue-deep: #0a4a8c;
    --blue-mid: #1565b0;
    --blue-bright: #2a8fd8;
    --blue-light: #6ec3ee;
    --name-blue: #7cc4ec;
    --ink: #2b2b2b;
    --white: #ffffff;
    --shadow: rgba(0, 0, 0, 0.35);
  }
  * { box-sizing: border-box; margin: 0; padding: 0; }
  html, body {
    width: 1200px;
    height: 900px;
    overflow: hidden;
    background: var(--page-bg);
    font-family: "Lato", Arial, sans-serif;
  }
  .canvas {
    position: relative;
    width: 1200px;
    height: 900px;
  }
  .card {
    position: absolute;
    left: 290px;
    width: 655px;
    height: 377px;
    overflow: hidden;
    box-shadow: 4px 6px 10px var(--shadow);
  }
  /* Front side */
  .card--front {
    top: 48px;
    background: linear-gradient(100deg, var(--blue-mid) 0%, var(--blue-deep) 100%);
  }
  .front-mark {
    position: absolute;
    left: -40px;
    top: -60px;
    width: 420px;
    height: 460px;
    border-radius: 50%;
    background: radial-gradient(circle at 35% 35%, var(--blue-light) 0%, var(--blue-bright) 55%, var(--blue-mid) 100%);
    opacity: 0.9;
  }
  .card--front .company-name {
    position: absolute;
    right: 40px;
    top: 218px;
    width: 300px;
    text-align: right;
    color: var(--white);
    font-weight: 700;
    font-size: 32px;
    line-height: 1.08;
  }
  /* Back side */
  .card--back {
    top: 485px;
    background: var(--white);
  }
  .card-back__shape {
    position: absolute;
    inset: 0;
    width: 655px;
    height: 377px;
  }
  .brand {
    position: absolute;
    left: 52px;
    top: 42px;
    display: flex;
    align-items: center;
    gap: 16px;
  }
  .brand__dot {
    width: 108px;
    height: 108px;
    border-radius: 50%;
    background: var(--blue-bright);
    flex: none;
  }
  .brand__name {
    color: var(--ink);
    font-weight: 700;
    font-size: 23px;
    line-height: 1.1;
    margin-top: -10px;
  }
  .person {
    position: absolute;
    left: 28px;
    width: 240px;
    top: 264px;
    text-align: center;
  }
  .person__name {
    color: var(--name-blue);
    font-weight: 700;
    font-size: 20px;
  }
  .person__role {
    color: var(--white);
    font-size: 15px;
    margin-top: 3px;
  }
  .divider {
    position: absolute;
    left: 279px;
    top: 237px;
    width: 2px;
    height: 110px;
    background: var(--white);
  }
  .contact {
    position: absolute;
    left: 322px;
    top: 238px;
    list-style: none;
    color: var(--white);
    font-size: 14.5px;
    line-height: 22.5px;
  }
  .contact__item {
    display: flex;
    align-items: center;
    gap: 6px;
    white-space: nowrap;
  }
  .contact__icon {
    width: 12px;
    height: 12px;
    flex: none;
    fill: var(--name-blue);
  }
</style>
</head>
<body>
<main class="canvas">

  <section class="card card--front" aria-label="Business card front">
    <div class="front-mark" role="img" aria-label="Large brand emblem area"></div>
    <p class="company-name">Tallbrook Meridian Advisory</p>
  </section>

  <section class="card card--back" aria-label="Business card back">
    <svg class="card-back__shape" viewBox="0 0 655 377" aria-hidden="true">
      <defs>
        <linearGradient id="backBlue" x1="0" y1="0" x2="1" y2="0.3">
          <stop offset="0" stop-color="#1a6cb6"/>
          <stop offset="1" stop-color="#0b4688"/>
        </linearGradient>
        <linearGradient id="greyBand" x1="0" y1="0" x2="1" y2="0">
          <stop offset="0" stop-color="#5c5e60"/>
          <stop offset="0.5" stop-color="#9a9c9e"/>
          <stop offset="1" stop-color="#c8c9ca"/>
        </linearGradient>
      </defs>
      <path d="M0 180 C 200 140 450 120 655 122 L655 377 L0 377 Z" fill="url(#greyBand)"/>
      <path d="M0 208 C 220 150 450 128 655 132 L655 377 L0 377 Z" fill="url(#backBlue)"/>
      <circle cx="600" cy="300" r="110" fill="#ffffff" opacity="0.06"/>
    </svg>

    <div class="brand">
      <span class="brand__dot" aria-hidden="true"></span>
      <p class="brand__name">Tallbrook Meridian<br>Advisory</p>
    </div>

    <div class="person">
      <p class="person__name">Mireille Vostag</p>
      <p class="person__role">Partner</p>
    </div>

    <span class="divider" aria-hidden="true"></span>

    <ul class="contact">
      <li class="contact__item">
        <svg class="contact__icon" viewBox="0 0 12 12" aria-hidden="true"><path d="M2.5 0.8 L4.3 3.2 L3.3 4.4 Q4.6 7 7.6 8.7 L8.8 7.7 L11.2 9.5 L10 11.3 Q4.5 10.8 0.7 2.2 Z"/></svg>
        +44 (0)781 209 3375
      </li>
      <li class="contact__item">
        <svg class="contact__icon" viewBox="0 0 12 12" aria-hidden="true"><path d="M0.5 2.5 H11.5 V10 H0.5 Z M1.3 3.2 L6 6.8 L10.7 3.2" stroke="#0b4688" stroke-width="0.8"/></svg>
        mireille_vostag@tallbrookmeridian.example
      </li>
      <li class="contact__item">
        <svg class="contact__icon" viewBox="0 0 12 12" aria-hidden="true"><circle cx="6" cy="6" r="5.5"/></svg>
        www.tallbrookmeridian.example
      </li>
      <li class="contact__item">17 Pelham Crescent, Brackwell</li>
      <li class="contact__item">Eastshire, UK, BW4 3WN</li>
    </ul>
  </section>

</main>
</body>
</html>
```